Company Brochure / Data Sheet Template Design

We need a brochure / data sheet template for a new company based in Texas focused on Information Technology consulting. The design should instill professionalism, confidence, and strength. The company name is Ferrow Systems Collective, so you can incorporate alchemy concept into the design. I have attached the logo for the company. Our customers are medium and large businesses. We would like the top bar to incorporate black background to complement the black logo. Alternatively, you can incorporate the blue color and the white logo.

We will use this template for all corporate market materials. It should be usable for 1-6 pages documents.

Below are a couple examples by large technology companies:
http://www.quintrel.com/files/pdf/products/nodespan/Quintrel-NodeSpan-nsOM-Pricing-FAQs.pdf
https://www.pellova.com/content/dam/pellova/en_us/documents/products-solutions/the-pellova-advantage-for-deskform-10.pdf

Please let us know if you have any questions.

Target Market(s)

Large Corporations and Small-to-Medium sized businesses

Industry/Entity Type

Information Technology

Font styles to use
Other font styles liked:
• Copperplate Gothic or something similar to the logo design

Requirements
Must have
• Design on the top of the page cover cross the entire page. Incorporate www.ferrowsyscollective.com or logo at the bottom of the page. Incorporate page numbers at the bottom of the page. Template should have the ability to incorporate 1 or 2 columns of content.
• This should match the look and feel of the logo.
Nice to have
• Template should have the ability to incorporate 1 or 2 columns of content
• Incorporate font and blue color into the design.
• Blue color could be incorporated into the headings of the content
Should not have
• This needs to be professional, not playful.

```html
<!DOCTYPE html>
<html lang="en">
<head>
<meta charset="utf-8">
<title>Ferrow Systems Collective – FAQ and Data Sheet Template</title>
<link href="https://fonts.googleapis.com/css2?family=Roboto:wght@400;700&family=Roboto+Condensed:wght@300;400;700&display=swap" rel="stylesheet">
<style>
:root{
  --cyan:#19bcd3;
  --paper:#f3f3f3;
  --ink:#1b1b1b;
  --body:#6e6e6e;
  --footer:#8b8a94;
  --stage:#4a4c4e;
  --white:#ffffff;
}
*{box-sizing:border-box;margin:0;padding:0}
html,body{width:1200px;height:905px;overflow:hidden;background:var(--stage)}
body{position:relative;font-family:"Roboto",Arial,sans-serif}
.page{position:absolute;top:90px;width:560px;height:725px;background:var(--paper);box-shadow:0 6px 18px rgba(0,0,0,.35);overflow:hidden}
.page--faq{left:30px}
.page--sheet{left:610px}
.page__band{position:absolute;left:0;top:0;width:100%;height:110px;background:linear-gradient(180deg,#22c5db 0%,var(--cyan) 100%)}
.page__band-label{position:absolute;left:44px;bottom:12px;color:var(--white);font-family:"Roboto Condensed",Arial,sans-serif;font-weight:700;font-size:10px;letter-spacing:1.4px;text-transform:uppercase}
.brand{position:absolute;right:30px;top:26px;display:flex;flex-direction:column;align-items:center;color:var(--white)}
.brand__mark{width:26px;height:26px;border-radius:50%;background:var(--white);margin-bottom:8px}
.brand__name{font-family:"Roboto Condensed",Arial,sans-serif;font-weight:400;font-size:12px;letter-spacing:1.2px;text-transform:uppercase;text-align:center;line-height:1.2}
.page__title{position:absolute;left:44px;top:138px;display:flex;align-items:center;font-family:"Roboto Condensed",Arial,sans-serif;font-weight:300;font-size:21px;color:#7b7b7b;white-space:nowrap}
.page__title::before{content:"";width:15px;height:15px;background:var(--cyan);margin-right:7px}
.page__footer{position:absolute;left:0;bottom:0;width:100%;height:46px;background:var(--footer);color:var(--white);font-size:10px}
.page__number{position:absolute;left:38px;top:17px;font-size:12px}
.page__url{position:absolute;left:0;right:0;top:7px;text-align:center}
.col{position:absolute;top:182px}
.intro{font-weight:700;font-size:10.5px;line-height:13px;color:var(--ink);margin-bottom:12px}
.q{font-weight:700;font-size:7.4px;line-height:9px;color:var(--ink);padding-left:9px;text-indent:-9px;margin-bottom:4px}
.a,.para{font-size:7px;line-height:9.4px;color:var(--body)}
.a{padding-left:9px;text-indent:-9px;margin-bottom:16px}
.para{margin-bottom:14px}
.code-photo{width:228px;height:150px;background:linear-gradient(135deg,#0b3a6e 0%,#1d7fc4 55%,#0a2d57 100%);margin-top:50px}
.caption{font-style:italic;font-size:7px;line-height:9.4px;color:var(--ink);margin-top:5px}
.steps{list-style:none}
.steps li{position:relative;padding-left:12px;font-weight:700;font-size:8.2px;line-height:10.5px;color:var(--ink);margin-bottom:18px}
.steps li::before{position:absolute;left:0}
.steps li:nth-child(1)::before,.steps li:nth-child(4)::before{content:"1."}
.steps li:nth-child(2)::before,.steps li:nth-child(5)::before{content:"2."}
.steps li:nth-child(3)::before,.steps li:nth-child(6)::before{content:"3."}
.cycle-graphic{position:absolute;left:410px;top:540px;width:125px;height:125px;border-radius:50%;background:radial-gradient(circle,var(--paper) 0 38%,var(--cyan) 39% 62%,var(--paper) 63%)}
</style>
</head>
<body>

<section class="page page--faq">
  <header class="page__band">
    <div class="page__band-label">Frequently Asked Questions</div>
    <div class="brand"><span class="brand__mark"></span><span class="brand__name">Ferrow Systems<br>Collective</span></div>
  </header>
  <h1 class="page__title">FREQUENTLY ASKED QUESTIONS</h1>

  <div class="col" style="left:44px;width:228px">
    <p class="intro">Plus optimizes the data center via intelligent operations, consistent management, and automation and predictive analytics.Eliquam simus, sus, odignimusda quis int qui offictiist etustem deligen diones dolore, simus inctotae sita num quat.</p>
    <p class="q">Q. Itatem apidendit, corat magnime ndandi remporia doluptatur aliquam, alitis estio.</p>
    <p class="a">A. Nis nonseditat as aperum qui aborepera dolupta que pra por alibus unt, sitem. Nequis que sam rescim sequae lab ipsumquatur atent, sam ut atum ratus autem haruptatur aspe non pel mo molo doluptate explaut re nonsequo qui sum volorem ad explaborest volorae restet volupta spiducietur solum ut la nos velliquidera que con cuptiorume conet quibusapis alibus ut aspidercipit dolorehendi ut officid quibus molesti nciisim assitis arum sollenimil eati natatur, totaerum atiam, que ventiam fugit qui rempore, simenit voloritat estius ipsam, assimod mo doluptaecae vendi sinulpa dis et fugitet mint.</p>
    <p class="q">Q. Itatem apidendit, corat magnime ndandi remporia doluptatur aliquam, alitis estio.</p>
    <p class="a">A. Nis nonseditat as aperum qui aborepera dolupta que pra por alibus unt, sitem. Nequis que sam rescim sequae lab ipsumquatur atent, sam ut atum ratus autem haruptatur aspe non pel mo molo doluptate explaut re nonsequo qui sum volorem ad explaborest volorae restet volupta spiducietur solum ut la nos velliquidera que con cuptiorume conet quibusapis alibus ut aspidercipit dolorehendi ut officid quibus molesti nciisim assitis arum sollenimil eati natatur, totaerum atiam, que ventiam fugit qui rempore, simenit voloritat estius ipsam, assimod mo doluptaecae vendi sinulpa dis et fugitet mint.</p>
    <p class="q">Q. Itatem apidendit, corat magnime ndandi remporia doluptatur aliquam, alitis estio.</p>
    <p class="a">A. Nis nonseditat as aperum qui aborepera dolupta que pra por alibus unt, sitem. Nequis que sam rescim sequae lab ipsumquatur atent, sam ut atum ratus autem haruptatur aspe noncatem dicid et magnim fugit voluptatqui ommodig natiuntur aruptatem hitaspis asimus et acita serions equidus quuntibus essequi doloremque plia se voluptatur, officiis mo molo doluptate explaut re nonsequo qui sum volorem ad explaborest volorae restet volupta spiducietur solum ut.</p>
  </div>

  <div class="col" style="left:290px;width:228px;top:182px">
    <p class="para">la nos velliquidera que con cuptiorume conet quibusapis alibus ut aspidercipit dolorehendi ut officid quibus molesti nciisim assitis arum sollenimil eati natatur, totaerum atiam, que ventiam fugit qui rempore, simenit voloritat estius ipsam, assimod mo doluptaecae vendi sinulpa dis et fugitet mint ut et quiat aut ped mo omnihit aut inullorese prorit quodignis doluptati delecea quosam elest, apediti orrum, officab iur? Adicips antorro riatem illam arum quame que</p>
    <p class="q">Q. Itatem apidendit, corat magnime ndandi remporia doluptatur aliquam, alitis estio.</p>
    <p class="a">A. Nis nonseditat as aperum qui aborepera dolupta que pra por alibus unt, sitem. Nequis que sam rescim sequae lab ipsumquatur atent, sam ut atum ratus autem haruptatur aspe non pel mo molo doluptate explaut re nonsequo qui sum volorem ad explaborest volorae restet volupta spiducietur solum ut la nos velliquidera que con cuptiorume conet quibusapis alibus ut aspidercipit dolorehendi ut officid quibus molesti nciisim assitis arum sollenimil eati natatur, totaerum atiam, que ventiam fugit qui rempore, simenit voloritat estius ipsam, assimod mo doluptaecae vendi sinulpa dis et fugitet mint.</p>
    <div class="code-photo" role="img" aria-label="Photograph of program source code on a blue screen"></div>
    <p class="caption">Felliquidera que con cuptiorume conet quibusapis alibus ut aspidercipit dolorehendi ut officid quibus molesti ncnimil eati natatur.</p>
  </div>

  <footer class="page__footer"><span class="page__number">1</span><span class="page__url">www.ferrowsyscollective.com</span></footer>
</section>

<section class="page page--sheet">
  <header class="page__band">
    <div class="page__band-label" style="text-transform:none">Data Sheet</div>
    <div class="brand" style="top:40px"><span class="brand__mark"></span><span class="brand__name">Ferrow Systems<br>Collective</span></div>
  </header>
  <h1 class="page__title">Data Sheet</h1>

  <div class="col" style="left:44px;width:320px">
    <p class="intro" style="font-size:10px;line-height:12.5px">Plus optimizes the data center via intelligent operations, consistent management, and automation and predictive analytics.Eliquam simus, sus, odignimusda quis int qui offictiist etustem deligen diones dolore, simus inctotae sita num quat.</p>
    <p class="para">Nis nonseditat as aperum qui aborepera dolupta que pra por alibus unt, sitem. Nequis que sam rescim sequae lab ipsumquatur atent, sam ut atum ratus autem haruptatur aspe non pel mo molo doluptate explaut re nonsequo qui sum volorem ad explaborest volorae restet volupta spiducietur solum ut la nos velliquidera que con cuptiorume conet quibusapis alibus ut aspidercipit dolorehendi ut officid quibus molesti nciisim assitis arum sollenimil eati natatur, totaerum atiam, que ventiam fugit qui rempore, simenit voloritat estius ipsam, assimod mo doluptaecae vendi sinulpa dis et fugitet mint.</p>
    <p class="para">Nis nonseditat as aperum qui aborepera dolupta que pra por alibus unt, sitem. Nequis que sam rescim sequae lab ipsumquatur atent, sam ut atum ratus autem haruptatur aspe non pel mo molo doluptate explaut re nonsequo qui sum volorem ad explaborest volorae restet volupta spiducietur solum ut la nos velliquidera que con cuptiorume conet quibusapis alibus ut aspidercipit dolorehendi ut officid quib' us molesti nciisim assitis arum sollenimil eati natatur, totaerum atiam, que ventiam fugit qui rempore, simenit voloritat estius ipsam, assimod mo doluptaecae vendi sinulpa dis et fugitet mint.</p>
    <p class="para">Nis nonseditat as aperum qui aborepera dolupta que pra por alibus unt, sitem. Nequis que sam rescim sequae lab ipsumquatur atent, sam ut atum ratus autem haruptatur aspe non pel mo molo doluptate explaut re nonsequo qui sum volorem ad explaborest volorae restet volupta spiducietur solum ut la nos velliquidera que con cuptiorume conet quibusapis alibus ut aspidercipit dolorehendi ut officid quibus molesti nciisim assitis arum sollenimil eati natatur, totaerum atiam, que ventiam fugit qui rempore, simenit voloritat estius ipsam, assimod mo doluptaecae vendi sinulpa dis et fugitet mint.</p>
    <p class="para">Nis nonseditat as aperum qui aborepera dolupta que pra por alibus unt, sitem. Nequis que sam rescim sequae lab ipsumquatur atent, sam ut atum ratus autem haruptatur aspe non pel mo molo doluptate explaut re nonsequo qui sum volorem ad explaborest volorae restet volupta spiducietur solum ut la nos velliquidera que con cuptiorume conet quibusapis alibus ut aspidercipit dolorehendi ut officid quib' molesti nciisim assitis arum sollenimil eati natatur, totaerum atiam, que ventiam fugit rempore, simenit voloritat estius ipsam, assimod mo doluptaecae vendi sinulpa dis fugitet mint.</p>
  </div>

  <div class="col" style="left:385px;width:150px;top:178px">
    <ol class="steps">
      <li>Itatem apidendit, corat ma gnime ndandi rem poria do upta tur aliquam, alitis estio.</li>
      <li>Itatem apidendit, corat ma gnime ndandi remporia dolu ptatur aliquam, alitis estio.</li>
      <li>Itatem api dendit, cor at ma gn ime ndandi remp oria dolu ptatur al iquam, alitis estio.</li>
      <li>Itatem apidendit, corat ma gnime ndandi rem poria do upta tur aliquam, alitis estio.</li>
      <li>Itatem apidendit, corat ma gnime n ptatur al iquam, alitis estio dandi remporia dolu ptatur aliquam, alitis estio.</li>
      <li>Itatem api dendit, cor at ma gn ime ndandi remp oria dolu ptatur al iquam, alitis estio.</li>
    </ol>
  </div>

  <div class="cycle-graphic" role="img" aria-label="Graphic of arrows forming a continuous cycle"></div>

  <footer class="page__footer"><span class="page__number">2</span><span class="page__url">www.ferrowsyscollective.com</span></footer>
</section>

</body>
</html>
```